Tellwick Asset Management - Corporate Letter Head Project

Looking for a classy design based on our current logo. Please find current logo source file in files. With our color scheme.

Target Market(s)

We're an investment firm, the letterhead needs to look professional and attractive to clients.

Industry/Entity Type

Hedgefund

Colors
0054AA
0677BA
7BADD7
CADEEF
E8F1F8

Requirements
Must have
• Our logo, address, phone number, and email

```html
<!DOCTYPE html>
<html lang="en">
<head>
<meta charset="utf-8">
<title>Tellwick Asset Management – Letterhead</title>
<link rel="stylesheet" href="https://fonts.googleapis.com/css2?family=Arimo:wght@400&family=Montserrat:wght@400;600;700&display=swap">
<style>
  :root {
    --backdrop: #9d9c9d;
    --paper: #ffffff;
    --navy: #1b2f55;
    --band: #14315a;
    --rule: #5a6b86;
    --text: #555559;
    --signature-tone: #e4e6ea;
  }
  * { margin: 0; padding: 0; box-sizing: border-box; }
  html, body {
    width: 906px; height: 1200px; overflow: hidden;
    background: var(--backdrop);
  }
  .letterhead {
    position: absolute; left: 104px; top: 107px;
    width: 698px; height: 986px;
    background: var(--paper);
    box-shadow: 3px 3px 5px rgba(0,0,0,0.35);
    overflow: hidden;
  }
  .brand-square {
    position: absolute; left: 95px; top: 31px;
    width: 52px; height: 52px;
    border: 1.2px solid var(--navy);
  }
  .brand-name {
    position: absolute; left: 30px; top: 94px; width: 172px;
    font-family: "Montserrat", sans-serif; font-weight: 600;
    color: var(--navy); text-align: center;
    font-size: 16.5px; letter-spacing: 0.2px; white-space: nowrap;
  }
  .header-rule {
    position: absolute; left: 40px; top: 121px;
    width: 618px; height: 0.8px; background: var(--rule);
  }
  .brand-tagline {
    position: absolute; left: 50px; top: 114px;
    padding: 0 3px; background: var(--paper);
    font-family: "Montserrat", sans-serif; font-weight: 600;
    font-size: 8.5px; letter-spacing: 6.6px;
    color: var(--navy); white-space: nowrap;
  }
  .contact {
    position: absolute; left: 524px; top: 38px;
    font-family: "Montserrat", sans-serif; font-weight: 400; font-style: normal;
    font-size: 11.5px; color: var(--text); line-height: 13.6px;
  }
  .contact-address { margin-bottom: 6px; }
  .contact-line { display: flex; align-items: center; gap: 6px; }
  .contact-line svg { width: 8px; height: 8px; flex: none; fill: var(--navy); }
  .letter { position: absolute; left: 63px; top: 0; width: 590px; color: var(--text); }
  .salutation {
    position: absolute; top: 302px; left: 1px;
    font-family: "Montserrat", sans-serif; font-weight: 600;
    font-size: 15.5px; white-space: nowrap;
  }
  .letter-body p {
    position: absolute; left: 0;
    font-family: "Arimo", sans-serif; font-size: 11.7px; line-height: 14.35px;
    white-space: nowrap;
  }
  .closing {
    position: absolute; top: 644px; left: 1px;
    font-family: "Montserrat", sans-serif; font-weight: 700; font-size: 8.6px;
  }
  .signature {
    position: absolute; top: 689px; left: 1px;
    width: 86px; height: 26px; background: var(--signature-tone);
  }
  .footer-band {
    position: absolute; left: 0; bottom: 0;
    width: 100%; height: 13px; background: var(--band);
  }
</style>
</head>
<body>
  <main class="letterhead">
    <header>
      <div class="brand-square"></div>
      <div class="brand-name">TELLWICK ASSET</div>
      <div class="header-rule"></div>
      <div class="brand-tagline">MANAGEMENT</div>

      <address class="contact">
        <div class="contact-address">Your address, city<br>state, ZIP 0000</div>
        <div class="contact-line">
          <svg viewBox="0 0 16 16" aria-hidden="true"><path d="M3 1l3 3-1.5 2a9 9 0 0 0 5.5 5.5L12 10l3 3-2 2C7 15 1 9 1 3z"/></svg>
          <span>555-014-2736</span>
        </div>
        <div class="contact-line">
          <svg viewBox="0 0 16 16" aria-hidden="true"><path d="M0 3h16v10H0z M0 3l8 6 8-6" stroke="#fff" stroke-width="1.2"/></svg>
          <span>youremail@mailbox.com</span>
        </div>
        <div class="contact-line">
          <svg viewBox="0 0 16 16" aria-hidden="true"><circle cx="8" cy="8" r="8"/><path d="M1 8h14M8 0c-4 4-4 12 0 16M8 0c4 4 4 12 0 16" stroke="#fff" stroke-width="1.1" fill="none"/></svg>
          <span>www.yourwebsite.com</span>
        </div>
      </address>
    </header>

    <section class="letter">
      <h1 class="salutation">Dear Mr. Smith,</h1>
      <div class="letter-body">
        <p style="top:349px">Lorem ipsum dolor sit amet, consectetuer adipiscing elit, sed diam nonmmy nibh euismod tincidunt ut laor<br>eet dolore magna aliquam erat volutpat. Ut wisi enim ad minim veniam, quis nostrud exerci tationmcorper<br>suscipit lobortis nisl ut aliquip ex ea commodo consequat. Duis autem vel eum iriure dolor in hendrerit in<br>vulputate velit esse molestie consequat, vel illum dolore eu feugiat</p>
        <p style="top:419px">Rorem ipsum dolor sit amet, consectetuer adipiscing elit, sed diam nonmmy nibh euismod tincidunt ut laor<br>eet dolore magna aliquam erat volutpat. Ut wisi enim ad minim veniam, quis nostrud exerci tationmcorper<br>suscipit lobortis nisl ut aliquip ex ea commodo consequat. Duis autem vel eum iriure dolor in hendrerit in<br>vulputate velit esse molest</p>
        <p style="top:490px">Dorem ipsum dolor sit amet, consectetuer adipiscing elit, sed diam nonmmy nibh euismod tincidunt ut laor<br>eet dolore magna aliquam erat volutpat. Ut wisi enim ad minim veniam, quis nostrud exerci tationmcorper<br>suscipit lobortis nisl ut aliquip ex ea commodo consequat. Duis autem vel eum iriure dolor in hendrerit in<br>suscipit lobortis nisl ut aliquip ex ea commodo consequat. Duis autem vel eum iriure dolor in hendrerit in<br>vulputate velit esse molestie consequat, vel illum</p>
        <p style="top:574px">Sorem ipsum dolor sit amet, consectetuer adipiscing elit, sed diam nonmmy nibh euismod tincidunt ut laor<br>eet dolore magna aliquam erat volutpat. Ut wisi enim ad minim veniam, quis nostrud exerci tationmcorper<br>suscipit lobortis nisl ut aliquip ex ea commodo consequat. Duis autem vel eum iriure dolor in</p>
      </div>
      <p class="closing">Sincerely,</p>
      <div class="signature" role="img" aria-label="Handwritten signature of the sender"></div>
    </section>

    <footer class="footer-band"></footer>
  </main>
</body>
</html>
```